Free UK Delivery Banner for website

We require a banner for a website which stated free delivery and then terms and conditions apply written at the bottom of it somewhere. Please visit the website as the banner must look correlated to the overall theme. the picture attached must also be edited to make it look slick. The FREE DELIVERY must be in a larger text and very visible. The terms & Conditions Apply should be in a really small text and the bottom corner of the banner. The banner must be 1900px X 960px

Target Market(s)

online website

Industry/Entity Type

fashion

Font styles to use
Serif
Sans Serif
Decorative
Script

Requirements
Must have
• Large free delivery and terms and conditions apply at the bottom
Nice to have
• make it look nice
Should not have
• Leave it to the designers

```html
<!DOCTYPE html>
<html lang="en">
<head>
<meta charset="utf-8">
<title>Free Delivery Banners</title>
<link href="https://fonts.googleapis.com/css2?family=Cormorant+Garamond:wght@500&family=Roboto:wght@300&display=swap" rel="stylesheet">
<style>
  :root {
    --page-bg: #e9e9e9;
    --sand: #dfdbcb;
    --ink: #121212;
    --night: #000000;
    --paper: #ffffff;
    --fine-light: #2a2a2a;
    --fine-dark: #9a9a9a;
    --sprig-light: #cfbfa4;
    --sprig-dark: #3b322b;
  }
  * { margin: 0; padding: 0; box-sizing: border-box; }
  html, body { width: 1200px; height: 1200px; overflow: hidden; }
  body { background: var(--page-bg); position: relative; }
  .banner {
    position: absolute;
    left: 190px;
    width: 820px;
    height: 414px;
    overflow: hidden;
  }
  .banner--sand { top: 159px; background: var(--sand); color: var(--ink); }
  .banner--night { top: 626px; background: var(--night); color: var(--paper); }
  .banner__photo { position: absolute; inset: 0; }
  .banner__sprig {
    position: absolute;
    left: 453px;
    top: 117px;
    width: 224px;
    height: 184px;
    border-radius: 50%;
  }
  .banner--sand .banner__sprig { background: radial-gradient(closest-side, var(--sprig-light), transparent); opacity: .55; }
  .banner--night .banner__sprig { background: radial-gradient(closest-side, var(--sprig-dark), transparent); opacity: .8; }
  .banner__headline {
    position: absolute;
    left: 352px;
    top: 172px;
    width: 432px;
    text-align: center;
    font-family: "Cormorant Garamond", serif;
    font-weight: 500;
    font-size: 61px;
    line-height: 1;
    letter-spacing: 0.5px;
    white-space: nowrap;
  }
  .banner__terms {
    position: absolute;
    right: 31px;
    top: 381px;
    font-family: "Roboto", sans-serif;
    font-weight: 300;
    font-size: 10px;
    letter-spacing: 0.1px;
  }
  .banner--sand .banner__terms { color: var(--fine-light); }
  .banner--night .banner__terms { color: var(--fine-dark); }
</style>
</head>
<body>
  <section class="banner banner--sand">
    <svg class="banner__photo" width="820" height="414" viewBox="0 0 820 414" role="img" aria-label="Photo of a rattan chair holding a mint green lace outfit and a black gift box with a thank you card">
      <defs>
        <linearGradient id="photoToneA" x1="0" y1="0" x2="0.3" y2="1">
          <stop offset="0" stop-color="#eef3cf"/>
          <stop offset="0.35" stop-color="#a9b58d"/>
          <stop offset="0.6" stop-color="#4a4538"/>
          <stop offset="0.85" stop-color="#5c5240"/>
          <stop offset="1" stop-color="#4c6e9a"/>
        </linearGradient>
      </defs>
      <polygon points="0,0 236,0 350,414 0,414" fill="url(#photoToneA)"/>
    </svg>
    <div class="banner__sprig" role="img" aria-label="Faint botanical sprig decoration"></div>
    <h1 class="banner__headline">FREE DELIVERY</h1>
    <p class="banner__terms">TERMS AND CONDITIONS APPLY</p>
  </section>

  <section class="banner banner--night">
    <svg class="banner__photo" width="820" height="414" viewBox="0 0 820 414" role="img" aria-label="Photo of a rattan chair holding a mint green lace outfit and a black gift box with a thank you card">
      <defs>
        <linearGradient id="photoToneB" x1="0" y1="0" x2="0.3" y2="1">
          <stop offset="0" stop-color="#eef3cf"/>
          <stop offset="0.35" stop-color="#a9b58d"/>
          <stop offset="0.6" stop-color="#4a4538"/>
          <stop offset="0.85" stop-color="#5c5240"/>
          <stop offset="1" stop-color="#4c6e9a"/>
        </linearGradient>
      </defs>
      <polygon points="0,0 236,0 350,414 0,414" fill="url(#photoToneB)"/>
    </svg>
    <div class="banner__sprig" role="img" aria-label="Faint botanical sprig decoration"></div>
    <h1 class="banner__headline">FREE DELIVERY</h1>
    <p class="banner__terms">TERMS AND CONDITIONS APPLY</p>
  </section>
</body>
</html>
```